Wren's Home Care Retractable Banner Design

Retractable Banner Design
We need a pull up retractable banner design
85 x 206 cm.
We need the banner to use at expo's, information sessions, presentations, recruitment days. Needs to be attractive to our elderly client's and staff (care workers)
Phone number needs to be on 08 6937 4426
Website also needs to be on the banner : wrenshomecare.com.au

Target Market(s)

35 +

Industry/Entity Type

aged care / community

Requirements
Must have
• Colours, fonts and logo as detailed in upload

```html
<!DOCTYPE html>
<html lang="en">
<head>
<meta charset="utf-8">
<title>Wren's Home Care – Pull Up Banner</title>
<link href="https://fonts.googleapis.com/css2?family=Poppins:wght@300;400;600&display=swap" rel="stylesheet">
<style>
  :root {
    --crimson: #931628;
    --white: #ffffff;
    --backdrop: #ecebe9;
    --photo-dark: #3a2a20;
    --photo-mid: #7a5a40;
    --photo-warm: #b7824a;
  }
  html, body {
    margin: 0;
    width: 1200px;
    height: 1200px;
    overflow: hidden;
    background: var(--backdrop);
    font-family: "Poppins", sans-serif;
  }
  .banner {
    position: absolute;
    left: 358px;
    top: 30px;
    width: 483px;
    height: 1140px;
    background: var(--white);
    overflow: hidden;
  }
  .banner-art {
    position: absolute;
    inset: 0;
  }
  .brand {
    position: absolute;
    left: 121px;
    top: 75px;
    display: flex;
    align-items: center;
    gap: 16px;
  }
  .brand-mark {
    width: 80px;
    height: 80px;
    border-radius: 50%;
    background: var(--crimson);
    flex: none;
  }
  .brand-name {
    color: var(--crimson);
    font-size: 30px;
    font-weight: 400;
    line-height: 1.05;
  }
  .brand-tagline {
    position: absolute;
    left: 218px;
    top: 164px;
    color: var(--crimson);
    font-size: 15px;
    font-weight: 400;
  }
  .headline {
    position: absolute;
    left: 44px;
    top: 336px;
    margin: 0;
    color: var(--white);
    font-size: 45px;
    line-height: 1.2;
    font-weight: 300;
  }
  .headline strong {
    display: block;
    font-weight: 600;
    font-size: 48px;
    line-height: 1.22;
  }
  .benefits {
    position: absolute;
    left: 48px;
    top: 866px;
    margin: 0;
    padding: 0;
    list-style: none;
    color: var(--white);
    font-size: 19px;
    font-weight: 400;
  }
  .benefits li {
    display: flex;
    align-items: center;
    gap: 14px;
    height: 39px;
  }
  .benefits li::before {
    content: "";
    width: 11px;
    height: 11px;
    border-radius: 50%;
    background: var(--white);
    flex: none;
  }
  .contact {
    position: absolute;
    left: 46px;
    top: 1044px;
    color: var(--white);
    font-size: 20px;
    font-weight: 400;
  }
  .contact-line {
    display: flex;
    align-items: center;
    gap: 16px;
    height: 41px;
  }
  .contact-icon {
    width: 18px;
    height: 18px;
    flex: none;
  }
</style>
</head>
<body>
  <main class="banner">
    <svg class="banner-art" viewBox="0 0 483 1140" width="483" height="1140" aria-hidden="false">
      <defs>
        <linearGradient id="photoTone" x1="0" y1="0" x2="1" y2="1">
          <stop offset="0" stop-color="var(--photo-mid)"/>
          <stop offset="0.5" stop-color="var(--photo-warm)"/>
          <stop offset="1" stop-color="var(--photo-dark)"/>
        </linearGradient>
      </defs>
      <rect class="photo-area" x="0" y="380" width="483" height="520" fill="url(#photoTone)" role="img" aria-label="Photo of a smiling care worker embracing an elderly man at home"/>
      <path class="headline-wave" fill="var(--crimson)"
        d="M0 330 C10 300 20 270 40 250 C80 215 160 222 240 232 C320 242 360 270 400 310 C440 345 470 360 483 372 L483 530 L0 680 Z"/>
      <path class="info-panel" fill="var(--crimson)"
        d="M0 866 C120 880 260 870 360 840 C420 822 460 800 483 782 L483 1025 L365 1140 L0 1140 Z"/>
      <path class="accent-arc" fill="none" stroke="var(--white)" stroke-width="1.4"
        d="M308 1022 C370 1012 430 980 445 928"/>
    </svg>

    <div class="brand">
      <span class="brand-mark"></span>
      <span class="brand-name">Wren's<br>Home Care</span>
    </div>
    <div class="brand-tagline">Your Home, Your Care</div>

    <h1 class="headline">After all its<strong>Your Home,<br>Your Care</strong></h1>

    <ul class="benefits">
      <li>Family-owned and local.</li>
      <li>Hassle-free,quality care.</li>
      <li>Peace of mind for families.</li>
      <li>Nurse-led expertise.</li>
    </ul>

    <div class="contact">
      <div class="contact-line">
        <svg class="contact-icon" viewBox="0 0 24 24" aria-hidden="true"><path fill="var(--white)" d="M6.6 10.8a15.1 15.1 0 0 0 6.6 6.6l2.2-2.2a1 1 0 0 1 1-.25 11.4 11.4 0 0 0 3.6.57 1 1 0 0 1 1 1V20a1 1 0 0 1-1 1A17 17 0 0 1 3 4a1 1 0 0 1 1-1h3.5a1 1 0 0 1 1 1c0 1.25.2 2.45.57 3.57a1 1 0 0 1-.25 1z"/></svg>
        <span>08 6937 4426</span>
      </div>
      <div class="contact-line">
        <svg class="contact-icon" viewBox="0 0 24 24" aria-hidden="true"><g fill="none" stroke="var(--white)" stroke-width="2"><circle cx="12" cy="12" r="9"/><path d="M3 12h18M12 3c3 3.2 3 14.8 0 18M12 3c-3 3.2-3 14.8 0 18"/></g></svg>
        <span>wrenshomecare.com.au</span>
      </div>
    </div>
  </main>
</body>
</html>
```